Business Card Design Project

for a second hand vintage clothing store. shop name is The Velvet Cupboard

Cards to be double sided

The name on the card is Joanna Whitfield

Information to put on card:

The Velvet Cupboard
Joanna Whitfield (no job title)
42/871 Dunmore St, Glenwick, Sydney, NSW, 2009.
Mobile: 0412 905 261
Email: thevelvetcupboard@mailbox.com.au
Web: www.thevelvetcupboard.com.au

Target Market(s)

Women looking at vintage clothing

Industry/Entity Type

Clothing

```html
<!DOCTYPE html>
<html lang="en">
<head>
<meta charset="utf-8">
<title>The Velvet Cupboard – Business Card</title>
<link rel="stylesheet" href="https://fonts.googleapis.com/css2?family=Source+Sans+3:wght@400&display=swap">
<style>
  :root {
    --backdrop: #2a2a2c;
    --plum: #5a2437;
    --cream: #f0dc9a;
    --amber: #e6901f;
    --rust: #d04a25;
    --ink-light: #f6ecd8;
  }
  * { margin: 0; padding: 0; box-sizing: border-box; }
  html, body {
    width: 1200px;
    height: 1200px;
    overflow: hidden;
    background: var(--backdrop);
    font-family: "Source Sans 3", "Myriad Pro", sans-serif;
  }
  .canvas {
    position: relative;
    width: 1200px;
    height: 1200px;
  }
  .card {
    position: absolute;
    left: 277px;
    width: 646px;
    height: 392px;
    background: var(--plum);
    overflow: hidden;
  }
  .card--front { top: 210px; }
  .card--back { top: 650px; }
  .card__swoosh {
    position: absolute;
    inset: 0;
    width: 100%;
    height: 100%;
  }
  .brand-name {
    position: absolute;
    color: var(--cream);
    font-weight: 400;
    white-space: nowrap;
    letter-spacing: 0.01em;
  }
  .card--front .brand-name {
    left: 22px;
    top: 188px;
    font-size: 25px;
  }
  .card--back .brand-name {
    left: 0;
    right: 0;
    top: 156px;
    text-align: center;
    font-size: 36px;
  }
  .contact {
    position: absolute;
    left: 323px;
    top: 142px;
    list-style: none;
    color: var(--ink-light);
    font-size: 14.5px;
    line-height: 26px;
    white-space: nowrap;
  }
</style>
</head>
<body>
<main class="canvas">

  <section class="card card--front" aria-label="Card front">
    <svg class="card__swoosh" viewBox="0 0 646 392" aria-hidden="true">
      <path d="M488,0 C590,55 650,150 638,220 C630,290 612,340 592,392 L646,392 L646,0 Z" fill="var(--cream)"/>
      <path d="M540,0 L646,0 L646,112 C622,62 588,26 540,0 Z" fill="var(--rust)"/>
      <path d="M646,286 L646,392 L604,392 C622,360 636,324 646,286 Z" fill="var(--rust)"/>
    </svg>
    <p class="brand-name">The Velvet Cupboard</p>
    <ul class="contact">
      <li>The Velvet Cupboard</li>
      <li>Joanna Whitfield (no job title)</li>
      <li>42/871 Dunmore St, Glenwick, Sydney, NSW, 2009.</li>
      <li>Mobile: 0412 905 261</li>
      <li>Email: thevelvetcupboard@mailbox.com.au</li>
      <li>Web: www.thevelvetcupboard.com.au</li>
    </ul>
  </section>

  <section class="card card--back" aria-label="Card back">
    <svg class="card__swoosh" viewBox="0 0 646 392" aria-hidden="true">
      <path d="M0,116 C70,230 300,300 646,232 L646,244 C380,328 120,318 0,214 Z" fill="var(--cream)"/>
      <path d="M0,228 C150,300 330,330 462,332 C320,350 130,336 0,292 Z" fill="var(--amber)"/>
    </svg>
    <p class="brand-name">The Velvet Cupboard</p>
  </section>

</main>
</body>
</html>
```